Opening Specials Flyer for SmileHaven Dental

We require a flyer design for our promotions/special offers for our new opening of Dental Practice. Please make one page flyer with designs on front and back
Opening Specials must be eye catchy, with images
FRONT - OPENING SPECIALS
BACK - MAP and Introduce our NEW CLINIC
on Back - MUST SAY "FLIP BACK OF FLYER TO VIEW OPENING SPECIAL OFFERS"

Opening specials to our local residents of West Ryde

Colour Scheme: Green, grey, white
Celebrate the opening of our new clinic
Opening Specials for West Ryde Residents include:

1. NO GAP Checkup for the whole family
NO GAP - Checkup Clean Fluoride X-rays - (to eligible health fund members)
2. Dental Crowns at half price - Full Ceramic $900 (includes core and crown, root canal extra) (please use picture of ceramic crown attached) - must bring voucher/flyer
3. Power tooth Whitening (Corvel Glint)- $400 must bring voucher/flyer
1hr office in chair whitening, immediate whitening results
4. 20% off all General Dental Treatment (must bring flyer- please design this onto flyer)
5. Free Healthcover Dental for Kids (for those eligible under Junior Oral Care Program up to $1000) - please have healthcover logo
6. Free consultation for second opinion of treatment plans

Emergency dental care available after hours, please contact (02) 7395 2268

Offer valid until 31st May 2016
by appointment only
No Gap for eligible health fund members only
Address: Shop 7/51-53 Larkin Rd West Ryde 2114
Please have image of atlas view of this location

Behind the flyer (back) I would like to introduce our new clinic:
MUST INCLUDE - Flip behind for opening special offers!

SmileHaven Dental is your Local Family Dentist
Newly opened in March 2016, we aim to provide local residents with affordable dentistry with a gentle friendly approach. We are a child friendly practice and welcome you and your family to visit our new clinic.

www.smilehavenclinic.com.au
info@smilehavenclinic.com.au
(02) 7395 2268

Target Market(s)

Residents of West Ryde and Surrounding Suburbs
Children and Family

Industry/Entity Type

Dental Clinic

Colors
acd036
b2b2b2

Requirements
Must have
• (You may phrase as you please)
• Newly Opened Dental Clinic in West Ryde
• Special Offers until 31st May 2016
• Specials and clearly big font "NO GAP"
• Healthcover logo (colour) next to "Free Healthcover Dental for Kids
• MUST have SmileHaven Dental Logo
• Must inform that voucher must be brought in order to claim specials
• Must have address: Shop 7/51-53 Larkin Rd West Ryde 2114
• Must have Ph: (02) 7395 2268
Nice to have
• Image of dental crown - full ceramic (attached)
• Image of Corvel Glint Whitening
• Map of Shop 7/51-53 Larkin Rd West Ryde (Atlas View)
• Happy family picture

```html
<!DOCTYPE html>
<html lang="en">
<head>
<meta charset="utf-8">
<title>SmileHaven Dental – Opening Specials Flyer</title>
<link rel="stylesheet" href="https://fonts.googleapis.com/css2?family=Great+Vibes&family=Oswald:wght@300;400;500&family=Roboto+Condensed:ital,wght@0,400;0,700;1,400&display=swap">
<style>
  :root{
    --green:#acd036;
    --green-dark:#8fb82a;
    --grey:#7a7a7a;
    --grey-mid:#b2b2b2;
    --grey-text:#5f5f5f;
    --white:#ffffff;
    --bg:#e8e8e5;
  }
  *{margin:0;padding:0;box-sizing:border-box}
  html,body{width:1200px;height:960px;overflow:hidden;background:var(--bg)}
  body{position:relative;font-family:"Roboto Condensed",Arial,sans-serif;color:var(--grey-text)}
  .flyer{position:absolute;top:80px;width:564px;height:800px;background:var(--white);overflow:hidden;box-shadow:0 4px 14px rgba(0,0,0,.18)}
  .flyer--front{left:24px}
  .flyer--back{left:612px}
  .flyer > *{position:absolute}
  .shapes{left:0;top:0;width:564px;height:800px}
  .caps{font-family:"Oswald",sans-serif;text-transform:uppercase}
  .brand{font-family:"Roboto Condensed",sans-serif;font-weight:700;color:var(--grey);line-height:1}
  .brand-name{display:flex;align-items:center;gap:6px;font-size:30px}
  .brand-dot{width:14px;height:14px;border-radius:50%;background:var(--green)}
  .brand-place{font-weight:400;font-size:16px;letter-spacing:1px;text-align:right;margin-top:2px}
  .script{font-family:"Great Vibes",cursive;color:var(--grey)}
  .photo-tooth{left:0;top:0}
  .circle-photo{border-radius:50%;border:3px solid var(--green)}
  .phone-line{display:flex;align-items:center;gap:6px;font-family:"Roboto Condensed",sans-serif;font-weight:700;color:var(--white);white-space:nowrap}
  .icon{width:16px;height:16px;fill:currentColor;flex:none}
  .map{border-radius:10px;border:4px solid #dfeeb4;background:linear-gradient(135deg,#ecebe3,#f4f1e6 55%,#e4e6d6)}
  .bar{background:var(--green);color:var(--white);font-family:"Oswald",sans-serif;text-transform:uppercase;font-size:17px;letter-spacing:.4px;border-radius:20px 0 0 20px;display:flex;align-items:center;justify-content:center;white-space:nowrap}

  /* emergency panels (shared) */
  .emergency{background:var(--grey);border-radius:0 0 14px 14px;color:var(--white);text-align:center}
  .emergency__title{position:absolute;left:0;right:0;font-family:"Oswald",sans-serif;font-weight:300;text-transform:uppercase;line-height:1.2}
  .emergency__contact{position:absolute;left:0;right:0}
  .emergency .phone-line{position:absolute;left:0;right:0;justify-content:center}

  /* front */
  .front-brand{left:34px;top:34px}
  .front-celebrate{left:270px;top:8px;font-size:62px;width:240px;text-align:center}
  .front-subtitle{left:222px;top:74px;width:320px;text-align:center;color:var(--green);font-size:16px;letter-spacing:1px;font-weight:300}
  .specials-heading{left:18px;top:124px;font-size:26px;color:var(--grey-text)}
  .specials-sub{left:18px;top:156px;font-size:12px}
  .no-gap{left:12px;width:200px;text-align:center;color:var(--white)}
  .no-gap__big{font-family:"Oswald",sans-serif;font-size:26px;line-height:1;font-weight:400}
  .no-gap__small{font-size:11px;font-weight:700;line-height:1.3;text-transform:uppercase}
  .no-gap__small em{font-style:normal;font-weight:400;text-transform:none}
  .no-gap--one{top:198px}
  .no-gap--two{top:258px}
  .emergency--front{left:12px;top:336px;width:190px;height:214px}
  .emergency--front .emergency__title{top:116px;font-size:17px}
  .emergency--front .emergency__contact{top:160px;font-size:15px}
  .emergency--front .phone-line{top:182px;font-size:21px}
  .discount-badge{left:52px;top:336px;width:114px;height:114px;border-radius:50%;background:var(--green);border:3px dashed var(--white);outline:5px solid var(--green);color:var(--white);text-align:center;padding-top:14px}
  .discount-badge__big{font-family:"Oswald",sans-serif;font-size:22px;line-height:1}
  .discount-badge__small{font-size:10px;font-weight:700;line-height:1.35}
  .discount-badge__note{font-size:10px;font-weight:700;color:#6d8a22;line-height:1.2}
  .offer{width:176px;text-align:center;font-size:12px;line-height:1.35}
  .offer__title{color:var(--green);font-weight:700;font-size:13px;text-transform:uppercase}
  .offer__title::before{content:"";display:inline-block;width:6px;height:6px;background:var(--grey-mid);margin-right:5px;vertical-align:middle}
  .offer__price{color:var(--green);font-family:"Oswald",sans-serif;font-size:24px;line-height:1.2}
  .offer__must{font-weight:700;text-transform:uppercase;font-size:11px}
  .offer--crowns{left:202px;top:440px}
  .offer--whitening{left:378px;top:440px}
  .kids{left:150px;top:596px;width:250px;text-align:center;font-size:12px;line-height:1.4}
  .kids .offer__title{font-size:14px}
  .kids b{color:var(--green)}
  .healthcover-star{left:414px;top:612px;width:18px;height:18px;border-radius:50%;background:#2fa7a1}
  .healthcover-badge{left:440px;top:606px;width:100px;height:30px;background:var(--green-dark)}
  .bar--consult{left:128px;top:658px;width:436px;height:30px}
  .front-map{left:28px;top:700px;width:154px;height:88px}
  .terms{left:220px;top:712px;width:330px;text-align:right;font-style:italic;font-size:13px;line-height:1.4}
  .terms span{color:var(--green)}
  .address-front{right:18px;top:770px;color:var(--white);font-weight:700;font-size:15px;display:flex;align-items:center;gap:6px}

  /* back */
  .back-title{right:40px;top:18px;text-align:right;line-height:1.1}
  .back-title__name{font-size:34px;color:var(--grey-text)}
  .back-title__tag{font-size:27px;color:var(--green)}
  .back-brand{left:30px;top:96px}
  .gentle{left:14px;top:226px;width:200px;text-align:center;color:var(--white);line-height:1}
  .gentle__big{font-family:"Oswald",sans-serif;font-weight:500;font-size:34px}
  .gentle__mid{font-family:"Oswald",sans-serif;font-weight:500;font-size:24px;margin-top:2px}
  .gentle__small{font-size:14px;font-weight:700;text-transform:uppercase;margin-top:6px}
  .emergency--back{left:14px;top:332px;width:188px;height:206px}
  .emergency--back .emergency__title{top:18px;font-size:20px}
  .emergency--back .emergency__contact{top:128px;font-size:16px}
  .emergency--back .phone-line{top:154px;font-size:22px}
  .intro-heading{left:222px;top:344px;width:330px;text-align:center;font-size:22px;line-height:1.15}
  .intro-text{left:222px;top:398px;width:330px;text-align:justify;font-size:19px;line-height:1.22}
  .bar--visit{left:130px;top:552px;width:434px;height:36px;font-size:19px}
  .book{left:40px;top:600px;width:500px;text-align:center;font-size:40px;white-space:nowrap}
  .back-map{left:30px;top:672px;width:206px;height:118px}
  .flip{left:330px;top:676px;width:218px;text-align:right;font-family:"Oswald",sans-serif;font-size:17px;line-height:1.2;color:var(--grey-text);text-transform:uppercase}
  .flip-arrow{left:318px;top:680px}
  .contacts{left:280px;top:738px;color:var(--white);font-weight:700;font-size:14px;line-height:1.3}
  .contacts li{list-style:none;display:flex;align-items:center;gap:6px}
  .contacts .icon{width:12px;height:12px}
</style>
</head>
<body>

<section class="flyer flyer--front" aria-label="Opening specials">
  <svg class="shapes" viewBox="0 0 564 800" aria-hidden="true">
    <path d="M0,118 C70,104 160,100 250,118" fill="none" stroke="var(--green)" stroke-width="2"/>
    <path d="M0,180 C90,170 180,172 250,190 L250,250 C350,262 450,252 564,238 L564,318 C450,320 330,328 250,330 L200,346 C130,354 60,358 0,362 Z" fill="var(--green)"/>
    <path d="M202,350 C330,330 450,322 564,318" fill="none" stroke="var(--grey-mid)" stroke-width="3"/>
    <path d="M0,768 C150,758 400,760 564,748 L564,800 L0,800 Z" fill="var(--green)"/>
  </svg>

  <svg class="photo-tooth" width="564" height="340" viewBox="0 0 564 340" role="img" aria-label="Photo of a smiling family of four outdoors">
    <defs>
      <linearGradient id="famFront" x1="0" y1="0" x2="1" y2="1">
        <stop offset="0" stop-color="#c7dca0"/><stop offset=".55" stop-color="#e5cdb6"/><stop offset="1" stop-color="#8fb0cf"/>
      </linearGradient>
    </defs>
    <path d="M228,140 C224,104 262,94 312,104 C342,110 352,124 374,124 C396,124 408,110 440,104 C490,94 532,104 528,140 L520,324 L236,324 Z" fill="url(#famFront)" stroke="#8a8a8a" stroke-width="7"/>
  </svg>

  <div class="brand front-brand">
    <div class="brand-name"><span class="brand-dot"></span>SmileHaven</div>
    <div class="brand-place">WEST RYDE</div>
  </div>
  <div class="script front-celebrate">Celebrate</div>
  <div class="caps front-subtitle">- The opening of our new clinic -</div>
  <div class="specials-heading">Opening Specials</div>
  <div class="specials-sub">for West Ryde Residents include:</div>

  <div class="no-gap no-gap--one">
    <div class="no-gap__big">▪NO GAP</div>
    <div class="no-gap__small">Checkup for the<br>whole family</div>
  </div>
  <div class="no-gap no-gap--two">
    <div class="no-gap__big">▪NO GAP</div>
    <div class="no-gap__small">Checkup clean fluoride<br>x-rays <em>(to eligible health fund members)</em></div>
  </div>

  <div class="emergency emergency--front">
    <div class="emergency__title">Emergency dental care<br>available after hours,</div>
    <div class="emergency__contact">please contact</div>
    <div class="phone-line">
      <svg class="icon" viewBox="0 0 24 24"><path d="M6.6 10.8a15.1 15.1 0 0 0 6.6 6.6l2.2-2.2a1 1 0 0 1 1-.25 11.4 11.4 0 0 0 3.6.57 1 1 0 0 1 1 1V20a1 1 0 0 1-1 1A17 17 0 0 1 3 4a1 1 0 0 1 1-1h3.5a1 1 0 0 1 1 1c0 1.25.2 2.46.57 3.6a1 1 0 0 1-.25 1Z"/></svg>
      02 7395 2268
    </div>
  </div>
  <div class="discount-badge">
    <div class="discount-badge__big">20% OFF</div>
    <div class="discount-badge__small">All General Dental<br>Treatment</div>
    <div class="discount-badge__note">(MUST BRING<br>FLYER)</div>
  </div>

  <div class="circle-photo" style="left:224px;top:306px;width:120px;height:120px;background:radial-gradient(circle at 45% 45%,#f4f4f2,#2a2a2a 62%)" role="img" aria-label="Photo of two full ceramic dental crowns"></div>
  <div class="circle-photo" style="left:406px;top:306px;width:120px;height:120px;background:linear-gradient(135deg,#f0ddc8,#e08a3a 55%,#cfd6dc)" role="img" aria-label="Photo of a patient receiving in-chair whitening treatment"></div>

  <div class="offer offer--crowns">
    <div class="offer__title">Dental Crowns</div>
    <div>at half price - <b>Full Ceramic</b></div>
    <div class="offer__price">$900</div>
    <div>(includes core and crown, root canal extra) <span class="offer__must">must bring voucher/flyer</span></div>
  </div>
  <div class="offer offer--whitening">
    <div class="offer__title">Power Tooth Whitening</div>
    <div><b>(Corvel Glint)</b></div>
    <div class="offer__price">$400</div>
    <div>1hr office in chair whitening, immediate whitening results.</div>
    <div class="offer__must">Must bring voucher/ flyer</div>
  </div>

  <div class="circle-photo" style="left:14px;top:560px;width:120px;height:120px;border-color:var(--grey-mid);background:linear-gradient(160deg,#dfe9c4,#f1d7c6 60%,#e8a9bd)" role="img" aria-label="Photo of a smiling young girl"></div>
  <div class="kids">
    <div class="offer__title">Free Healthcover Dental for Kids</div>
    <div>(for those eligible under Junior Oral Care Program up to <b>$1000</b>)</div>
  </div>
  <div class="healthcover-star" aria-hidden="true"></div>
  <div class="healthcover-badge" role="img" aria-label="Healthcover partner badge"></div>

  <div class="bar bar--consult">Free consultation for second opinion of treatment plans</div>
  <div class="map front-map" role="img" aria-label="Atlas View map of Larkin Rd, West Ryde"></div>
  <div class="terms"><span>*</span> Offer valid until 31st May 2016 by appointment only<br><span>*</span> No Gap for eligible health fund members only</div>
  <div class="address-front">
    <svg class="icon" viewBox="0 0 24 24"><path d="M12 2a7 7 0 0 0-7 7c0 5 7 13 7 13s7-8 7-13a7 7 0 0 0-7-7Zm0 9.5A2.5 2.5 0 1 1 12 6.5a2.5 2.5 0 0 1 0 5Z"/></svg>
    Shop 7/51-53 Larkin Rd West Ryde 2114
  </div>
</section>

<section class="flyer flyer--back" aria-label="Clinic introduction">
  <svg class="shapes" viewBox="0 0 564 800" aria-hidden="true">
    <path d="M0,176 C90,158 180,152 250,150" fill="none" stroke="var(--green)" stroke-width="2"/>
    <path d="M0,182 C90,176 170,176 220,184 L220,300 C330,312 450,300 564,284 L564,326 C440,330 320,334 220,336 L202,336 L0,362 Z" fill="var(--green)"/>
    <path d="M202,338 C330,330 450,326 564,322" fill="none" stroke="var(--grey-mid)" stroke-width="3"/>
    <path d="M0,746 C150,736 400,730 564,722 L564,800 L0,800 Z" fill="var(--green)"/>
  </svg>

  <svg class="photo-tooth" width="564" height="340" viewBox="0 0 564 340" role="img" aria-label="Photo of a smiling family of four sitting together at home">
    <defs>
      <linearGradient id="famBack" x1="0" y1="0" x2="1" y2="1">
        <stop offset="0" stop-color="#eadfcf"/><stop offset=".5" stop-color="#e0c0a4"/><stop offset="1" stop-color="#b8c6b0"/>
      </linearGradient>
    </defs>
    <path d="M214,140 C210,104 248,94 300,104 C332,110 344,124 368,124 C392,124 404,110 438,104 C490,94 534,104 530,140 L522,316 L222,316 Z" fill="url(#famBack)" stroke="#8a8a8a" stroke-width="7"/>
  </svg>

  <div class="back-title">
    <div class="back-title__name">SmileHaven Dental</div>
    <div class="back-title__tag">is your Local Family Dentist</div>
  </div>
  <div class="brand back-brand">
    <div class="brand-name" style="font-size:32px"><span class="brand-dot"></span>SmileHaven</div>
    <div class="brand-place">WEST RYDE</div>
  </div>

  <div class="gentle">
    <div class="gentle__big">GENTLE</div>
    <div class="gentle__mid">DENTISTRY</div>
    <div class="gentle__small">for the whole family</div>
  </div>

  <div class="emergency emergency--back">
    <div class="emergency__title">Emergency<br>dental care<br>available<br>after hours,</div>
    <div class="emergency__contact">please contact</div>
    <div class="phone-line">
      <svg class="icon" viewBox="0 0 24 24"><path d="M6.6 10.8a15.1 15.1 0 0 0 6.6 6.6l2.2-2.2a1 1 0 0 1 1-.25 11.4 11.4 0 0 0 3.6.57 1 1 0 0 1 1 1V20a1 1 0 0 1-1 1A17 17 0 0 1 3 4a1 1 0 0 1 1-1h3.5a1 1 0 0 1 1 1c0 1.25.2 2.46.57 3.6a1 1 0 0 1-.25 1Z"/></svg>
      02 7395 2268
    </div>
  </div>

  <div class="intro-heading">We are NEW Dental Clinic<br>in West Ryde</div>
  <p class="intro-text">Newly opened in March 2016, we aim to provide local residents with affordable dentistry with a gentle friendly approach. We are a child friendly practice and welcome you and your family to visit our new clinic.</p>

  <div class="bar bar--visit">Come and see us for professional service and care</div>
  <div class="script book">Book a dental appointment today!</div>

  <div class="map back-map" role="img" aria-label="Atlas View map of Larkin Rd, West Ryde"></div>
  <svg class="flip-arrow" width="24" height="40" viewBox="0 0 24 40" aria-hidden="true">
    <path d="M18,4 C6,10 4,22 10,32" fill="none" stroke="var(--green)" stroke-width="4"/>
    <path d="M3,28 L11,38 L17,27 Z" fill="var(--green)"/>
  </svg>
  <div class="flip">Flip back of flyer to view<br>opening special offers</div>

  <ul class="contacts">
    <li><svg class="icon" viewBox="0 0 24 24"><path d="M12 2a7 7 0 0 0-7 7c0 5 7 13 7 13s7-8 7-13a7 7 0 0 0-7-7Zm0 9.5A2.5 2.5 0 1 1 12 6.5a2.5 2.5 0 0 1 0 5Z"/></svg>Shop 7/51-53 Larkin Rd West Ryde 2114</li>
    <li><svg class="icon" viewBox="0 0 24 24"><circle cx="12" cy="12" r="10" fill="none" stroke="currentColor" stroke-width="2.5"/><path d="M2 12h20M12 2c3 3 3 17 0 20M12 2c-3 3-3 17 0 20" fill="none" stroke="currentColor" stroke-width="2"/></svg>www.smilehavenclinic.com.au</li>
    <li><svg class="icon" viewBox="0 0 24 24"><path d="M2 5h20v14H2Z M2 5l10 8 10-8" fill="none" stroke="currentColor" stroke-width="2.5"/></svg>info@smilehavenclinic.com.au</li>
  </ul>
</section>

</body>
</html>
```